Business Card Design

We need a business card design for a Non-Profit Christian Based Organization located in Milford, Pa.
Alder Ridge Open Door Relief
Is a Christ-centered organization dedicated to providing compassion and hope to homeless or near homeless, families and individuals, by meeting their basic and urgent need of food, clothing and shelter.
Updates
the logo is black and white
and must add the color green some where 00400
Industry/Entity Type
Clothing
Contact Information for Business Card
Alder Ridge Open Door Relief
P.O. Box 817
Fernbrook, Pa 18492
Phone: (570) 384-CARE(2273)
Toll Free: (855) 384-CARE
email:Info@alderridgeodr.org
email:Careline@alderridgeodr.org
Our organization already has a logo.
Front of card:
Is a Christ-centered organization dedicated to providing compassion and hope to homeless or near homes, families and individual by meeting their basic and urgent need of food, clothing and shelter.(this is our Mission Statement)
On back of card:
'I was hungry and you gave me something to eat;
"I was thirsty and you gave me something to drink;
"I was a stranger and you invited me in."
Matthew 25:35
Color: Logo is black and white
Background color I would like a bright light green 00ff00(close to that)
I attached a sample of what I created on Quill Press but, I don't like the color green, nor the design (but I just wanted to give you and Idea of the Logo and Alder Ridge (one line) Open Door Relief (second line) in a different font thank you
Colette Marsh
Pr/Board of Directors

```html
<!DOCTYPE html>
<html lang="en">
<head>
<meta charset="utf-8">
<title>Alder Ridge Open Door Relief – Business Card</title>
<link href="https://fonts.googleapis.com/css2?family=Antonio:wght@200;300&display=swap" rel="stylesheet">
<style>
  :root {
    --page: #ffffff;
    --card: #e6e6e6;
    --green: #6abf45;
    --ink: #1a1a1a;
  }
  * { margin: 0; padding: 0; box-sizing: border-box; }
  html, body { width: 1200px; height: 857px; overflow: hidden; background: var(--page); }
  body {
    position: relative;
    font-family: "Antonio", "Arial Narrow", sans-serif;
    font-weight: 300;
    color: var(--ink);
  }
  .card {
    position: absolute;
    left: 252px;
    width: 696px;
    height: 387px;
    background: var(--card);
    border: 7px solid var(--green);
  }
  .card--front { top: 51px; }
  .card--back { top: 454px; }

  .org-name {
    position: absolute;
    left: 53px; top: 75px;
    font-size: 37px;
    font-weight: 300;
    line-height: 1;
    letter-spacing: -0.5px;
    white-space: nowrap;
  }
  .contact {
    position: absolute;
    left: 53px; top: 117px;
    font-size: 14px;
    line-height: 21.5px;
    font-style: normal;
    white-space: nowrap;
  }
  .accent { color: var(--green); }

  .logo-mark {
    position: absolute;
    left: 150px; top: 220px;
    display: flex;
    align-items: center;
    gap: 8px;
    font-size: 16px;
    line-height: 1.2;
  }
  .logo-mark__square {
    width: 18px; height: 18px;
    background: var(--ink);
    flex: none;
  }

  .mission {
    position: absolute;
    left: 368px; top: 196px;
    width: 280px;
    font-size: 14px;
    line-height: 21.5px;
    text-align: justify;
    text-align-last: right;
  }

  .verse {
    position: absolute;
    left: 158px; top: 130px;
    font-size: 22px;
    line-height: 33px;
    letter-spacing: -0.2px;
    white-space: nowrap;
  }
  .verse__ref {
    position: absolute;
    right: 189px; top: 234px;
    font-size: 22px;
    font-style: normal;
    color: var(--green);
    white-space: nowrap;
  }
</style>
</head>
<body>
  <section class="card card--front">
    <h1 class="org-name">Alder Ridge Open Door Relief</h1>
    <address class="contact">
      P.O. Box 817 Fernbrook, Pa 18492 ~ Phone: (570) 384-<span class="accent">CARE</span>(2273)<br>
      Toll Free Number: (855)-384-<span class="accent">CARE</span>(2273)<br>
      Info@alderridgeodr.org ~ Careline@alderridgeodr.org
    </address>
    <div class="logo-mark">
      <span class="logo-mark__square"></span>
      <span>Alder Ridge<br>Open Door Relief</span>
    </div>
    <p class="mission">"Alder Ridge Open Door Relief is a Christ-centered organization dedicated to providing compassion and hope to homeless or near-homeless, families and individuals by meeting their basic and urgent needs of food, clothing and shelter"</p>
  </section>

  <section class="card card--back">
    <blockquote class="verse">
      “I was hungry and you gave me something to eat;<br>
      I was thirsty and you gave me something to drink;<br>
      I was a stranger and you invited me in.”
    </blockquote>
    <cite class="verse__ref">( Matthew 25:35 )</cite>
  </section>
</body>
</html>
```